A new updated business card. A good first impression for new customers to our business.

I need something unique. I will attached a picture of our old rubbish cards, and also our current Logo ( I think this needs an update if you have any ideas, its very basic and budget)The best way you will get to see my business is checking our Facebook page, I don't really know what else to say, but anything you want to know, ask away.www.facebook.com/tkwsurfacewashing/

Target Market(s)

Home owners

Industry/Entity Type

Business

Contact Information for Business Card

T&K's Surface Washing & Paving Glazing
Mira 0462 318 905 mira@tkwsurfacewashing.com
Dunstan 0458 621 370 dunstan@tkwsurfacewashing.com

FB: www.facebook.com/tkwsurfacewashing/
Website: www.tkwsurfacewashing.net (This is pretty rubbish- we don't really use it)

100% customer satisfaction guaranteed

All aspects of Hi-Pressure Cleaning
Sealing & Re-Sealing
Roof Cleaning
Colour sealing
Decorative coatings

Free no obligation quotes

Requirements
Must have
• NO OBLIGATION FREE quotes
• 100% Customer satisfaction guaranteed
• Can you please add both names, contact details and email address on one card.
• Dunstan 0458 621 370
• dunstan@tkwsurfacewashing.com
• Mira 0462 318 905
• mira@tkwsurfacewashing.com
• Please change the services:
• Hot/Cold Hi-Pressure Cleaning
• Sealing & Re-Sealing
• Roof Cleaning
• Colour Sealing
• Decorative Coatings
• Concrete Honing
• Thanks
Nice to have
• Something a bit different, something eye catching.l

```html
<!DOCTYPE html>
<html lang="en">
<head>
<meta charset="utf-8">
<title>T&amp;K's Surface Washing &amp; Paving Glazing – Business Card</title>
<link rel="stylesheet" href="https://fonts.googleapis.com/css2?family=Open+Sans:wght@400;600;700&display=swap">
<style>
  :root {
    --bg: #ece8e3;
    --card-white: #ffffff;
    --brand-red: #f40b0b;
    --stripe-blue: #47b9ea;
    --text-light: #ffffff;
    --shadow: rgba(0, 0, 0, 0.18);
  }
  * { box-sizing: border-box; margin: 0; padding: 0; }
  html, body {
    width: 1200px; height: 900px; overflow: hidden;
    background: var(--bg);
    font-family: "Open Sans", Arial, sans-serif;
  }
  .canvas { position: relative; width: 1200px; height: 900px; }
  .card {
    position: absolute;
    width: 640px; height: 366px;
    background: var(--card-white);
    box-shadow: 0 10px 26px var(--shadow);
    overflow: hidden;
  }
  .card--front { left: 120px; top: 70px; }
  .card--back { left: 440px; top: 464px; }

  .card__top {
    height: 160px;
    display: flex; align-items: center; justify-content: center;
  }
  .brand { display: flex; align-items: center; gap: 14px; }
  .brand__dot {
    width: 22px; height: 22px; border-radius: 50%;
    background: var(--brand-red);
  }
  .brand__name {
    color: var(--brand-red);
    font-weight: 700; font-size: 27px; line-height: 1.15;
    text-align: center;
  }
  .card__stripe { height: 5px; background: var(--stripe-blue); }
  .card__gap { height: 5px; }
  .card__bottom {
    position: absolute; left: 0; right: 0; top: 170px; bottom: 0;
    background: var(--brand-red);
    color: var(--text-light);
  }

  /* front */
  .promise {
    text-align: center; font-weight: 700; font-size: 23px;
    margin-top: 16px; line-height: 1.3;
  }
  .services {
    list-style: none;
    display: grid; grid-template-columns: 1fr 1fr;
    column-gap: 36px; row-gap: 8px;
    width: 580px; margin: 14px auto 0;
    font-size: 16px; font-weight: 600; line-height: 1.35;
  }
  .services li { display: flex; align-items: center; gap: 9px; white-space: nowrap; }
  .services li::before, .services li::after {
    width: 8px; height: 8px; border-radius: 50%;
    background: var(--text-light); flex: none;
  }
  .services__item--left { justify-content: flex-end; }
  .services__item--left::after { content: ""; }
  .services__item--right::before { content: ""; }
  .quotes {
    text-align: center; font-weight: 700; font-size: 16px;
    letter-spacing: 0.04em; text-transform: uppercase;
    margin-top: 14px;
  }

  /* back */
  .contacts {
    display: grid; grid-template-columns: 320px 300px;
    column-gap: 20px;
    padding-top: 22px;
    font-size: 16px;
  }
  .contact { display: flex; flex-direction: column; gap: 9px; }
  .contact--left { align-items: flex-end; text-align: right; }
  .contact--right { align-items: flex-start; }
  .contact__name { font-weight: 700; font-size: 21px; line-height: 1.1; }
  .contact__row { display: flex; align-items: center; gap: 9px; white-space: nowrap; }
  .icon { width: 15px; height: 15px; flex: none; fill: var(--text-light); }
  .icon-dot {
    width: 14px; height: 14px; border-radius: 50%;
    background: var(--text-light); flex: none;
  }
</style>
</head>
<body>
<main class="canvas">

  <section class="card card--front" aria-label="Business card front">
    <div class="card__top">
      <div class="brand">
        <span class="brand__dot"></span>
        <div class="brand__name">T&amp;K's Surface Washing<br>&amp; Paving Glazing</div>
      </div>
    </div>
    <div class="card__stripe"></div>
    <div class="card__gap"></div>
    <div class="card__bottom">
      <p class="promise">100% customer satisfaction guaranteed</p>
      <ul class="services">
        <li class="services__item--left">Hot/Cold Hi-Pressure Cleaning</li>
        <li class="services__item--right">Sealing &amp; Re-Sealing</li>
        <li class="services__item--left">Colour Sealing</li>
        <li class="services__item--right">Roof Cleaning</li>
        <li class="services__item--left">Decorative Coatings</li>
        <li class="services__item--right">Concrete Honing</li>
      </ul>
      <p class="quotes">No obligation free quotes</p>
    </div>
  </section>

  <section class="card card--back" aria-label="Business card back">
    <div class="card__top">
      <div class="brand">
        <span class="brand__dot"></span>
        <div class="brand__name">T&amp;K's Surface Washing<br>&amp; Paving Glazing</div>
      </div>
    </div>
    <div class="card__stripe"></div>
    <div class="card__gap"></div>
    <div class="card__bottom">
      <div class="contacts">
        <div class="contact contact--left">
          <span class="contact__name">Mira</span>
          <span class="contact__row">0462 318 905
            <svg class="icon" viewBox="0 0 24 24" aria-hidden="true"><path d="M6.6 10.8c1.4 2.8 3.8 5.1 6.6 6.6l2.2-2.2c.3-.3.7-.4 1-.2 1.1.4 2.3.6 3.6.6.6 0 1 .4 1 1V20c0 .6-.4 1-1 1C10.6 21 3 13.4 3 4c0-.6.4-1 1-1h3.5c.6 0 1 .4 1 1 0 1.3.2 2.5.6 3.6.1.3 0 .7-.2 1l-2.3 2.2z"/></svg>
          </span>
          <span class="contact__row">mira@tkwsurfacewashing.com
            <svg class="icon" viewBox="0 0 24 24" aria-hidden="true"><path d="M3 5h18v14H3z M4.5 6.5 12 12l7.5-5.5" fill="none" stroke="#fff" stroke-width="2"/></svg>
          </span>
          <span class="contact__row">tkwsurfacewashing <span class="icon-dot"></span></span>
        </div>
        <div class="contact contact--right">
          <span class="contact__name">Dunstan</span>
          <span class="contact__row">
            <svg class="icon" viewBox="0 0 24 24" aria-hidden="true"><path d="M6.6 10.8c1.4 2.8 3.8 5.1 6.6 6.6l2.2-2.2c.3-.3.7-.4 1-.2 1.1.4 2.3.6 3.6.6.6 0 1 .4 1 1V20c0 .6-.4 1-1 1C10.6 21 3 13.4 3 4c0-.6.4-1 1-1h3.5c.6 0 1 .4 1 1 0 1.3.2 2.5.6 3.6.1.3 0 .7-.2 1l-2.3 2.2z"/></svg>
            0458 621 370</span>
          <span class="contact__row">
            <svg class="icon" viewBox="0 0 24 24" aria-hidden="true"><path d="M3 5h18v14H3z M4.5 6.5 12 12l7.5-5.5" fill="none" stroke="#fff" stroke-width="2"/></svg>
            dunstan@tkwsurfacewashing.com</span>
          <span class="contact__row">
            <svg class="icon" viewBox="0 0 24 24" aria-hidden="true"><g fill="none" stroke="#fff" stroke-width="2"><circle cx="12" cy="12" r="9"/><ellipse cx="12" cy="12" rx="4" ry="9"/><path d="M3 12h18"/></g></svg>
            www.tkwsurfacewashing.net</span>
        </div>
      </div>
    </div>
  </section>

</main>
</body>
</html>
```